Letterhead Creation

I would like to create a letterhead incorporating my family crest attached. My current letterhead with my information is also attached. I would also like to add my Paralegal Marisol Dunleavy

```html
<!DOCTYPE html>
<html lang="en">
<head>
<meta charset="utf-8">
<title>Law Offices of Jacqueline R Vasquez — Letterhead</title>
<link rel="stylesheet" href="https://fonts.googleapis.com/css2?family=Sorts+Mill+Goudy&display=swap">
<style>
  :root {
    --paper: #ffffff;
    --ink: #2a2a2a;
    --crest-blue: #2447a3;
    --crest-light: #e9edf7;
  }
  html, body {
    margin: 0;
    padding: 0;
    width: 1200px;
    height: 1200px;
    overflow: hidden;
    background: var(--paper);
  }
  .letterhead {
    position: relative;
    width: 1200px;
    height: 1200px;
    background: var(--paper);
    font-family: "Sorts Mill Goudy", Georgia, serif;
    color: var(--ink);
  }
  .crest {
    position: absolute;
    left: 490px;
    top: 26px;
    width: 196px;
    height: 170px;
  }
  .firm-name {
    position: absolute;
    left: 0;
    right: 0;
    top: 202px;
    margin: 0;
    text-align: center;
    font-weight: 400;
    font-size: 26px;
    line-height: 32px;
    letter-spacing: 1.6px;
    color: var(--ink);
  }
  .contact {
    position: absolute;
    top: 250px;
    margin: 0;
    font-size: 20.5px;
    font-weight: 400;
    line-height: 42.5px;
    letter-spacing: 0.6px;
    white-space: nowrap;
    font-style: normal;
  }
  .contact span { display: block; }
  .contact--address { left: 43px; }
  .contact--lines { left: 881px; }
</style>
</head>
<body>
  <main class="letterhead">
    <svg class="crest" viewBox="0 0 196 170" role="img" aria-label="Family crest: blue shield with chevron beneath a knight's helm and foliage mantling">
      <defs>
        <radialGradient id="crestTone" cx="50%" cy="55%" r="60%">
          <stop offset="0%" stop-color="var(--crest-blue)"/>
          <stop offset="70%" stop-color="#6f86c6"/>
          <stop offset="100%" stop-color="var(--crest-light)"/>
        </radialGradient>
      </defs>
      <rect x="0" y="0" width="196" height="170" rx="20" fill="url(#crestTone)"/>
    </svg>

    <h1 class="firm-name">LAW OFFICES OF JACQUELINE R VASQUEZ</h1>

    <address class="contact contact--address">
      <span class="contact__name">Jacqueline Vasquez Esq</span>
      <span class="contact__paralegal">Marisol Dunleavy, Paralegal</span>
      <span>4170. Alderwood</span>
      <span>Glendora, CA., 91740</span>
    </address>

    <address class="contact contact--lines">
      <span>Telephone (555) 218 - 4067</span>
      <span>Fax &nbsp;&nbsp;(555) &nbsp;- 730 - 1952</span>
      <span>Email: Jackie@Vasqlawpc.com</span>
    </address>
  </main>
</body>
</html>
```